wooden jewelry - pearl necklaces

I sell wooden jeweler (rings and pearls) on markets, and so on. I also opened my business as a carpenter. The rings and a combination of wood and metal. The wood is special wood, not very common on Europe. I paint the rings afterwards. You can see some of the pictures on the pictures I uploaded. The pearls are made of the same kind of wood and colored in all kinds of colors. They are then assembled to bracelets. The jewelry is very individual and looks really cool and all kinds of people.

Target Market(s)

Young urban alternative with a sense of individuality

Contact Information for Business Card

Front:

Text:

„Kugelwerk“ (big)
„Malte Oswitz“ (smaler)

Back
„Holzschmuck
Herstellung von individuellem Holz- und Modeschmuck

Malte Oswitz
Tel: 015239460518
Lindgarbweg 9
83127 Tannried

malteoswitz@postfeld.de“

Font styles to use
Sans Serif

Requirements
Nice to have
• Nice to see a camel thorn tree on the background, this is a special wood and some of the rings are made out of this wood.

```html
<!DOCTYPE html>
<html lang="de">
<head>
<meta charset="utf-8">
<title>Kugelwerk – Visitenkarte</title>
<link rel="stylesheet" href="https://fonts.googleapis.com/css2?family=Jost:wght@500;600;700&family=EB+Garamond:ital@1&display=swap">
<style>
  :root {
    --page: #ffffff;
    --ink: #0c0c0c;
    --on-photo: #ffffff;
    --label: #3d8c7c;
    --bead-dark: #2a1d2e;
    --bead-wood: #b5703a;
    --bead-light: #e8c88a;
    --bead-red: #b8284a;
    --bead-navy: #23264f;
    --sky-peach: #f7cdb0;
    --sky-rose: #e9c3bf;
    --ground-blue: #d7e4f1;
  }
  * { margin: 0; padding: 0; box-sizing: border-box; }
  html, body { width: 1200px; height: 1200px; overflow: hidden; background: var(--page); }
  .sheet { position: relative; width: 1200px; height: 1200px; font-family: "Jost", "Futura", sans-serif; }

  .card { position: absolute; overflow: hidden; }
  .card--front { left: 220px; top: 10px; width: 850px; height: 520px; }
  .card--back { left: 210px; top: 614px; width: 850px; height: 518px; }

  .bead-photo {
    position: absolute; inset: 0;
    background:
      radial-gradient(circle at 18% 22%, var(--bead-red) 0 4%, transparent 9%),
      radial-gradient(circle at 62% 70%, var(--bead-navy) 0 6%, transparent 13%),
      radial-gradient(circle at 85% 30%, var(--bead-navy) 0 5%, transparent 12%),
      radial-gradient(circle at 35% 60%, var(--bead-wood) 0 8%, transparent 16%),
      radial-gradient(circle at 75% 15%, var(--bead-light) 0 7%, transparent 15%),
      radial-gradient(circle at 10% 80%, var(--bead-light) 0 7%, transparent 15%),
      linear-gradient(135deg, var(--bead-wood), var(--bead-dark) 45%, var(--bead-wood) 70%, var(--bead-light));
  }
  .tree-photo {
    position: absolute; inset: 0;
    background: linear-gradient(180deg, var(--sky-peach) 0%, var(--sky-rose) 55%, var(--ground-blue) 82%, var(--ground-blue) 100%);
  }

  .brand-name, .owner-front {
    position: absolute; left: 0; right: 0; text-align: center; color: var(--on-photo); font-weight: 700; line-height: 1; white-space: nowrap;
  }
  .brand-name { top: 130px; font-size: 142px; letter-spacing: 2px; }
  .owner-front { top: 293px; font-size: 84px; letter-spacing: 2px; }

  .line { position: absolute; color: var(--ink); font-weight: 700; line-height: 1; text-align: center; white-space: nowrap; }
  .trade__title { left: 0; width: 850px; top: 63px; font-size: 50px; letter-spacing: 1px; }
  .trade__tagline { left: 0; width: 850px; top: 112px; font-size: 28px; letter-spacing: 0.6px; }
  .contact { position: absolute; left: 0; top: 0; width: 850px; height: 518px; font-style: normal; }
  .contact .line { left: 300px; width: 500px; }
  .contact__name { top: 178px; font-size: 68px; letter-spacing: 1.5px; }
  .contact__tel { top: 250px; font-size: 42px; letter-spacing: 1.5px; }
  .contact__street { top: 294px; font-size: 42px; letter-spacing: 1.5px; }
  .contact__city { top: 338px; font-size: 42px; letter-spacing: 1.5px; }
  .contact__email { top: 428px; font-size: 40px; letter-spacing: 0.8px; }

  .side-label {
    position: absolute; font-family: "EB Garamond", "Palatino", serif; font-style: italic;
    color: var(--label); font-size: 96px; line-height: 1;
  }
  .side-label--front { left: 466px; top: 516px; }
  .side-label--back { left: 520px; top: 1112px; }
</style>
</head>
<body>
<main class="sheet">
  <section class="card card--front">
    <div class="bead-photo" role="img" aria-label="Photo of colourful painted wooden beads in a heap"></div>
    <h1 class="brand-name">Kugelwerk</h1>
    <p class="owner-front">Malte Oswitz</p>
  </section>
  <p class="side-label side-label--front">front</p>

  <section class="card card--back">
    <div class="tree-photo" role="img" aria-label="Faded photo of dead camel thorn trees on a pale desert plain at dusk"></div>
    <h2 class="line trade__title">Holzschmuck</h2>
    <p class="line trade__tagline">Herstellung von individuellem Holz- und Modeschmuck</p>
    <address class="contact">
      <p class="line contact__name">Malte Oswitz</p>
      <p class="line contact__tel">Tel: 015239460518</p>
      <p class="line contact__street">Lindgarbweg 9</p>
      <p class="line contact__city">83127 Tannried</p>
      <p class="line contact__email">malteoswitz@postfeld.de</p>
    </address>
  </section>
  <p class="side-label side-label--back">back</p>
</main>
</body>
</html>
```